Postcard design for accounting company

We need a postcard design (front and back) to our accounting firm that provides bookkeeping services to small and mid-size companies using LedgerPad Online. We would like to see designs that use the color blue and match our overall branding (see website). The final design should communicate professionalism, trust, and ease.

Target Market(s)

Small and Mid-Size companies

Industry/Entity Type

Accounting

Colors
0054AA
0677BA
7BADD7
CADEEF
E8F1F8

Requirements
Must have
• Logo, contact information, indicate services offered, color blue, and fit postcard template (see attached). Contact info = 555.318.2207, 1.800.555.0142, Info@BrightLedgerAccounting.com, www.BrightLedgerAccounting.com. Use the ZRPX Retail Indicia, which is a postage payment mark that takes the place of a regular postage stamp or meter stamp. Every ZRPX mailpiece must include the ZRPX Retail Indicia above and to the right of the address block. The ZRPX Retail Indicia does not have a specific size requirement but must be larger than 0.5" x 0.5". The type font must be in all caps and at least a 4 point size. It should fit in the area 1.625" from the right edge and 1.375" from top edge. Leave 1/8" of space around the top and right edge. See attached sample.
Nice to have
• Include that we a re Certified LedgerPad CertPartners (can include LPO logo). Also, maybe include the logos of the associations we are members of (North Pinecrest Chamber of Commerce, Federal Guild of Certified Ledgerkeepers, and Continental League of Female Enterprise Founders.

```html
<!DOCTYPE html>
<html lang="en">
<head>
<meta charset="utf-8">
<title>Bright Ledger Accounting – Postcard Front and Back</title>
<link href="https://fonts.googleapis.com/css2?family=Fira+Sans:wght@400;500;600;700;800&family=Lato:wght@400;700&display=swap" rel="stylesheet">
<style>
  :root {
    --navy: #1b4a86;
    --blue: #0054aa;
    --mid-blue: #0677ba;
    --title-blue: #1a7fc1;
    --teal: #35b5cf;
    --sky: #7badd7;
    --pale: #cadeef;
    --mist: #eef1f7;
    --ink: #1d2433;
    --rule: #c9ced6;
    --backdrop: #a6a6a6;
    --white: #ffffff;
  }
  * { box-sizing: border-box; margin: 0; padding: 0; }
  html, body { width: 1200px; height: 904px; overflow: hidden; background: var(--backdrop); }
  body { position: relative; font-family: "Lato", sans-serif; }

  .postcard {
    position: absolute;
    width: 982px; height: 661px;
    background: var(--white);
    overflow: hidden;
    transform-origin: top left;
    transform: scale(0.5425);
    box-shadow: 0 6px 18px rgba(0,0,0,.25);
  }
  .postcard--front { left: 148px; top: 74px; }
  .postcard--back  { left: 535px; top: 471px; }

  .abs { position: absolute; }

  /* brand name */
  .brand {
    display: flex; align-items: center; gap: 12px;
    font-family: "Fira Sans", sans-serif; font-weight: 700;
    color: var(--navy); line-height: 1.05;
  }
  .brand__square { background: var(--blue); flex: none; }

  /* front */
  .front__brand { left: 44px; top: 52px; font-size: 38px; width: 380px; }
  .front__brand .brand__square { width: 48px; height: 48px; }

  .front__photo { left: 0; top: 0; width: 982px; height: 600px; }

  .headline-band {
    left: 0; top: 195px; width: 480px; height: 165px;
    background: var(--teal);
    color: var(--white);
    font-family: "Fira Sans", sans-serif;
    padding: 22px 0 0 40px;
  }
  .headline-band__main { font-size: 62px; font-weight: 700; letter-spacing: 1.5px; line-height: 1; }
  .headline-band__sub { font-size: 39px; font-weight: 800; margin-top: 6px; letter-spacing: .3px; }

  .specialty-band {
    left: 0; top: 360px; width: 560px; height: 118px;
    background: var(--mist);
    display: flex; align-items: center; gap: 18px;
    padding-left: 40px;
  }
  .specialty-band__dot { width: 76px; height: 76px; border-radius: 50%; background: var(--mid-blue); flex: none; }
  .specialty-band__text {
    font-family: "Fira Sans", sans-serif; font-weight: 500;
    color: var(--navy); font-size: 21.5px; line-height: 1.27;
  }

  .quote-cta {
    left: 38px; top: 498px;
    font-family: "Fira Sans", sans-serif; font-weight: 800;
    color: var(--navy); font-size: 27px; line-height: 1.27;
  }
  .memberships { left: 283px; top: 495px; display: flex; gap: 14px; align-items: center; }
  .membership-badge { width: 70px; height: 70px; border-radius: 50%; background: var(--pale); border: 3px solid var(--sky); }

  .contact-bar {
    left: 0; width: 982px; height: 66px;
    background: linear-gradient(180deg, var(--mid-blue), var(--navy));
    display: flex; align-items: center; justify-content: space-between;
    padding: 0 36px;
    color: var(--white);
    font-family: "Lato", sans-serif; font-weight: 700; font-size: 16.5px;
  }
  .front .contact-bar { top: 595px; }
  .contact-bar__item { display: flex; align-items: center; gap: 10px; white-space: nowrap; }
  .contact-bar__icon { width: 19px; height: 19px; flex: none; }

  /* back */
  .services-tab {
    left: 0; top: 30px; width: 240px; height: 36px;
    background: var(--navy);
    color: var(--white);
    font-family: "Fira Sans", sans-serif; font-weight: 800; font-size: 24px;
    padding: 3px 0 0 40px;
    clip-path: polygon(0 0, 100% 0, 94% 100%, 0 100%);
  }
  .services-tab__accent { left: 232px; top: 30px; width: 16px; height: 36px; background: var(--teal); clip-path: polygon(40% 0, 100% 0, 60% 100%, 0 100%); }

  .service { left: 38px; width: 520px; }
  .service__icon { float: left; width: 84px; height: 84px; margin: 0 8px 0 0; shape-outside: circle(50%); }
  .service__title {
    font-family: "Fira Sans", sans-serif; font-weight: 700;
    color: var(--title-blue); font-size: 20px; line-height: 1.1;
    padding-left: 100px;
  }
  .service__body { font-size: 16.4px; line-height: 1.33; color: var(--ink); text-align: justify; }
  .service--bookkeeping { top: 72px; }
  .service--reporting { top: 215px; width: 500px; }
  .service--payroll { top: 360px; width: 455px; }

  .certified-band {
    left: 0; top: 488px; width: 560px; height: 108px;
    background: var(--mist);
  }
  .certified-band__text {
    position: absolute; left: 38px; top: 22px; width: 360px;
    font-family: "Fira Sans", sans-serif; font-weight: 500;
    color: var(--navy); font-size: 16.5px; line-height: 1.3; text-align: justify;
  }
  .certified-badge { position: absolute; left: 414px; top: 0; width: 72px; height: 96px; background: var(--white); border: 1px solid var(--rule); }
  .certified-badge__mark { position: absolute; left: 14px; top: 62px; width: 44px; height: 22px; background: var(--sky); }

  .back__brand { left: 622px; top: 40px; font-size: 24px; width: 200px; }
  .back__brand .brand__square { width: 30px; height: 30px; }

  .indicia {
    left: 862px; top: 40px; width: 80px; height: 80px;
    border: 1px solid var(--rule);
    font-family: "Fira Sans", sans-serif; font-weight: 600;
    font-size: 10.4px; line-height: 1.3; text-align: center;
    color: var(--ink); text-transform: uppercase;
    padding-top: 6px;
  }
  .address-line { left: 615px; width: 327px; height: 2px; background: var(--rule); }

  .back .contact-bar { top: 596px; height: 65px; }
</style>
</head>
<body>

<!-- Front of postcard -->
<section class="postcard postcard--front front" aria-label="Postcard front">
  <svg class="abs front__photo" viewBox="0 0 982 600" role="img" aria-label="Photo of a person using a calculator over financial papers, with a laptop showing an online bookkeeping dashboard">
    <defs>
      <linearGradient id="photoTone" x1="0" y1="0" x2="1" y2="1">
        <stop offset="0" stop-color="#b9a58a"/>
        <stop offset=".45" stop-color="#dfe3e8"/>
        <stop offset="1" stop-color="#c7d3e2"/>
      </linearGradient>
    </defs>
    <path d="M510 0 C440 160 440 380 640 520 L640 600 H982 V0 Z" fill="url(#photoTone)"/>
  </svg>

  <svg class="abs" style="left:0;top:0" width="982" height="600" viewBox="0 0 982 600" aria-hidden="true">
    <path d="M560 446 Q440 330 447 195 Q450 130 470 95" fill="none" stroke="var(--blue)" stroke-width="8" stroke-linecap="round"/>
    <polygon points="486,66 456,88 484,104" fill="var(--blue)"/>
  </svg>

  <div class="abs brand front__brand">
    <span class="brand__square"></span>
    <span>Bright Ledger Accounting</span>
  </div>

  <div class="abs headline-band">
    <div class="headline-band__main">ACCOUNTING</div>
    <div class="headline-band__sub">FOR YOUR BUSINESS</div>
  </div>

  <div class="abs specialty-band">
    <span class="specialty-band__dot"></span>
    <p class="specialty-band__text">Specializing in Cloud-Based<br>Bookkeeping &amp; Payroll Processing<br>with LedgerPad Online by Corvane.</p>
  </div>

  <p class="abs quote-cta">REQUEST A FREE<br>QUOTE TODAY!</p>

  <div class="abs memberships" aria-label="Association memberships">
    <span class="membership-badge" title="North Pinecrest Chamber of Commerce"></span>
    <span class="membership-badge" title="Continental League of Female Enterprise Founders"></span>
    <span class="membership-badge" title="Federal Guild of Certified Ledgerkeepers"></span>
  </div>

  <footer class="abs contact-bar">
    <span class="contact-bar__item">
      <svg class="contact-bar__icon" viewBox="0 0 20 20"><path d="M5 2 L8 6 L6 8 Q8 12 12 14 L14 12 L18 15 L16 18 Q8 18 2 6 Z" fill="none" stroke="var(--pale)" stroke-width="1.8"/></svg>
      <span>555.318.2207 / 1.800.555.0142</span>
    </span>
    <span class="contact-bar__item">
      <svg class="contact-bar__icon" viewBox="0 0 20 20"><rect x="2" y="5" width="16" height="11" fill="none" stroke="var(--pale)" stroke-width="1.8"/><path d="M2 5 L10 11 L18 5" fill="none" stroke="var(--pale)" stroke-width="1.8"/></svg>
      <span>info@brightledgeraccounting.com</span>
    </span>
    <span class="contact-bar__item">
      <svg class="contact-bar__icon" viewBox="0 0 20 20"><circle cx="10" cy="10" r="8" fill="none" stroke="var(--pale)" stroke-width="1.8"/><ellipse cx="10" cy="10" rx="3.5" ry="8" fill="none" stroke="var(--pale)" stroke-width="1.5"/><path d="M2 10 H18" stroke="var(--pale)" stroke-width="1.5"/></svg>
      <span>www.brightledgeraccounting.com</span>
    </span>
  </footer>
</section>

<!-- Back of postcard -->
<section class="postcard postcard--back back" aria-label="Postcard back">
  <svg class="abs" style="left:0;top:0" width="982" height="600" viewBox="0 0 982 600" aria-hidden="true">
    <path d="M535 0 Q610 120 580 300 Q560 440 530 600" fill="none" stroke="var(--teal)" stroke-width="7"/>
    <path d="M590 200 Q585 380 520 520 Q500 570 540 600" fill="none" stroke="var(--navy)" stroke-width="12"/>
  </svg>

  <div class="abs services-tab">OUR SERVICES:</div>
  <div class="abs services-tab__accent"></div>

  <article class="abs service service--bookkeeping">
    <svg class="service__icon" viewBox="0 0 84 84" aria-hidden="true">
      <circle cx="42" cy="42" r="40" fill="var(--navy)" stroke="var(--sky)" stroke-width="3"/>
      <rect x="26" y="22" width="24" height="34" fill="none" stroke="#fff" stroke-width="2.5"/>
      <rect x="40" y="36" width="18" height="24" fill="var(--navy)" stroke="#fff" stroke-width="2.5"/>
      <path d="M30 30 H44 M30 36 H38" stroke="#fff" stroke-width="2"/>
    </svg>
    <h2 class="service__title">BOOKKEEPING</h2>
    <p class="service__body">Let us take over the day to day bookkeeping so you can get back to running your business. We offer LedgerPad Online setup and ongoing bookkeeping, including daily journal entries, accounts payables &amp; receivables, bill pay, sales tax reporting &amp; payments, account reconciliation, and more.</p>
  </article>

  <article class="abs service service--reporting">
    <svg class="service__icon" viewBox="0 0 84 84" aria-hidden="true">
      <circle cx="42" cy="42" r="40" fill="var(--navy)" stroke="var(--sky)" stroke-width="3"/>
      <rect x="26" y="20" width="28" height="40" fill="none" stroke="#fff" stroke-width="2.5"/>
      <path d="M32 52 V44 M38 52 V38 M44 52 V42" stroke="#fff" stroke-width="3"/>
      <circle cx="56" cy="54" r="7" fill="var(--navy)" stroke="#fff" stroke-width="2.5"/>
    </svg>
    <h2 class="service__title">FINANCIAL REPORTING</h2>
    <p class="service__body">We'll provide easy to understand financial reports that allow you &amp; your team to manage cash flow, create budgets &amp; make forecasting decisions. Want real time data? Let us provide solutions with the latest in mobile apps &amp; dashboards.</p>
  </article>

  <article class="abs service service--payroll">
    <svg class="service__icon" viewBox="0 0 84 84" aria-hidden="true">
      <circle cx="42" cy="42" r="40" fill="var(--navy)" stroke="var(--sky)" stroke-width="3"/>
      <rect x="34" y="18" width="24" height="42" rx="3" fill="none" stroke="#fff" stroke-width="2.5"/>
      <circle cx="34" cy="46" r="9" fill="var(--navy)" stroke="#fff" stroke-width="2.5"/>
      <path d="M27 53 L20 60" stroke="#fff" stroke-width="3"/>
    </svg>
    <h2 class="service__title">PAYROLL PROCESSING</h2>
    <p class="service__body">Whether you have 5 employees or 100+, payroll can be an overwhelming and time consuming task. We offer full service payroll processing, including employee onboarding and reporting.</p>
  </article>

  <div class="abs certified-band">
    <p class="certified-band__text">Our Certified LedgerPad CertPartners have the Knowledge and Expertise to Ensure Professional, Accurate, High Quality Service.</p>
    <div class="certified-badge" aria-label="Certified partner badge"><span class="certified-badge__mark"></span></div>
  </div>

  <div class="abs brand back__brand">
    <span class="brand__square"></span>
    <span>Bright Ledger Accounting</span>
  </div>

  <div class="abs indicia">PRSRT STD<br>ECRWSS<br>U.S.POSTAGE<br>PAID<br>ZRPX Retail</div>

  <span class="abs address-line" style="top:283px"></span>
  <span class="abs address-line" style="top:347px"></span>
  <span class="abs address-line" style="top:411px"></span>

  <footer class="abs contact-bar">
    <span class="contact-bar__item">
      <svg class="contact-bar__icon" viewBox="0 0 20 20"><path d="M5 2 L8 6 L6 8 Q8 12 12 14 L14 12 L18 15 L16 18 Q8 18 2 6 Z" fill="none" stroke="var(--pale)" stroke-width="1.8"/></svg>
      <span>555.318.2207 / 1.800.555.0142</span>
    </span>
    <span class="contact-bar__item">
      <svg class="contact-bar__icon" viewBox="0 0 20 20"><rect x="2" y="5" width="16" height="11" fill="none" stroke="var(--pale)" stroke-width="1.8"/><path d="M2 5 L10 11 L18 5" fill="none" stroke="var(--pale)" stroke-width="1.8"/></svg>
      <span>info@brightledgeraccounting.com</span>
    </span>
    <span class="contact-bar__item">
      <svg class="contact-bar__icon" viewBox="0 0 20 20"><circle cx="10" cy="10" r="8" fill="none" stroke="var(--pale)" stroke-width="1.8"/><ellipse cx="10" cy="10" rx="3.5" ry="8" fill="none" stroke="var(--pale)" stroke-width="1.5"/><path d="M2 10 H18" stroke="var(--pale)" stroke-width="1.5"/></svg>
      <span>www.brightledgeraccounting.com</span>
    </span>
  </footer>
</section>

</body>
</html>
```